Presentation Brochure and Sample Box Design for Verix Board

Verix Board is our range of aluminium composite panel that our company supplies to the signage and shop fitting industries.
the range is divided into 3 sections: Signage Grade - Light Commercial Grade and Commercial Grade.
We require an, A4 double-sided folding brochure (swatch book) that folds 3 ways, opening once and then a second time to lay out 3 pages flat.

There should be a front and back cover.

The inside cover should be reserved with text blocks for written information about the composite panel.

The opposite page on the right when you first open the brochure should have all our Commercial Grade colours, which are the timber finishes and the 4mm black, white and metallic silver.

When the brochure is folded out a second time, showing all three inside pages flat, the two inside pages on the right (next to the inside cover with the written information) should show all our Signage Grade colours, followed by the Light Commercial Grade colours.
Each colour in each section should have the product code beneath the swatch.

This brochure should have a modern and professional feel suitable for presenting to signees, shop fitters and interiors designers.

We also require a box design to contain aluminium composite panel samples of all the colours in the range.

Please refer to the template attached for the box dimensions and layout.

The box should tie in with the brochure as a complete package with a modern and professional look suitable for presenting to shop fitters and interior designers.

Finally we require a small label sticker to be stuck on the back of each sample. On the sticker should be the Verix Board logo, a space to put the product code for the sample colour and the phone number 1300 584 962.

To summarise, this package project includes:
1 tri-folding A4 brochure,
1 sample box package design
1 sample sticker label.

Please refer to the attachments for the Verix Board logo in two formats - the colour swatch book and template for the sample box.
The Logo may be shown with either the original blue text or with the text in white. The blue icon colour should not change.

Target Market(s)

Signage, shop fitting and interior design

Font styles to use
Serif
Sans Serif

Requirements
Must have
• A modern, neat and professional upmarket look suitable for presenting to shop fitters and interior designers.
Nice to have
• A slick and classy look that makes you want to take home the box or brochure even if you're not interested in the product.
Should not have
• A cheap, untidy, low market look with too many colours.

```html
<!DOCTYPE html>
<html lang="en">
<head>
<meta charset="utf-8">
<title>Verix Board – Aluminium Composite Panel Guide</title>
<link rel="stylesheet" href="https://fonts.googleapis.com/css2?family=Open+Sans:wght@400;600;700;800&family=Montserrat:wght@500;700&display=swap">
<style>
:root{
  --bg:#2a2a2c;
  --navy:#233a7b;
  --blue:#2f8fd8;
  --ink:#1f2f66;
  --paper:#ffffff;
  --paper-tint:#e6eef8;
  --rule:#9aa6c2;
  --swatch-line:#6f6f74;
  --empty:#d1d2d5;
}
*{margin:0;padding:0;box-sizing:border-box}
html,body{width:1200px;height:1171px;overflow:hidden;background:var(--bg);font-family:"Open Sans",Arial,sans-serif}
.canvas{position:relative;width:1200px;height:1171px;background:var(--bg)}
.spread{position:absolute;left:87px;width:1026px;height:483px;background:var(--paper);overflow:hidden;box-shadow:0 4px 12px rgba(0,0,0,.45)}
.spread--outside{top:83px}
.spread--inside{top:605px}
.page{position:absolute;top:0;width:342px;height:483px;background:linear-gradient(90deg,var(--paper-tint),var(--paper) 35%)}
.page--1{left:0}.page--2{left:342px}.page--3{left:684px}
.band{position:absolute;background:var(--navy)}
.tab{position:absolute;top:0;height:44px;background:var(--navy);clip-path:polygon(0 0,100% 0,92% 100%,8% 100%)}
.tab--left{clip-path:polygon(0 0,100% 0,100% 100%,10% 100%)}
.wordmark{position:absolute;display:flex;align-items:center;gap:6px;font-family:"Montserrat",sans-serif;font-weight:500;letter-spacing:.14em;white-space:nowrap}
.wordmark i{display:block;background:var(--blue)}
.wordmark--light{color:#fff}
.wordmark--dark{color:var(--ink)}
.heading{position:absolute;font-weight:600;color:var(--ink);font-size:11.5px;line-height:1.2;padding-bottom:2px;border-bottom:1px solid var(--rule);white-space:nowrap}
.heading--small{font-size:11px;line-height:1.25}
.grid{position:absolute;display:grid;grid-template-columns:repeat(4,64px);column-gap:9px}
.swatch{width:64px;height:36px;border:1px solid var(--swatch-line);border-radius:4px;background:#fff;display:flex;align-items:flex-end;justify-content:center;padding:0 12px 5px;font-size:4.4px;font-weight:700;text-align:center;line-height:1.1;color:#222;text-transform:uppercase}
.swatch.dark{color:#fff}
.black{background:#0a0a0a}.red{background:#e21f26}.yellow{background:#efe21c}
.process{background:#1e86c9}.reflex{background:#2d3688}.forest{background:#0f4a36}
.heritage{background:#7a1e2c}.orange{background:#ef5726}.navyblue{background:#13264f}
.charcoal{background:#cfcec6}.emerald{background:#179b48}.msilver{background:#cacac6}
.steel{background:#171d2e}.brush{background:linear-gradient(135deg,#d8d8d8,#9a9a9a 50%,#e6e6e6)}
.raw{background:#c8c9cb}.undercoat{background:#cfd0d2}
.copper{background:linear-gradient(135deg,#c08457,#a86a42)}.gold{background:linear-gradient(135deg,#a8893a,#86702e)}
.embossed{background:linear-gradient(135deg,#d7d7d7,#9d9d9d,#e2e2e2)}
.rust{background:#9b3b23}
.wood-golden{background:linear-gradient(90deg,#8a4f24,#b06a35,#7d4720)}
.wood-walnut{background:linear-gradient(90deg,#6e3415,#8f4b22,#5f2d13)}
.wood-allspice{background:linear-gradient(90deg,#5b3520,#7a4a2c,#4d2c1a)}
.wood-wenge{background:linear-gradient(90deg,#3d2618,#5b3c28,#33200f)}
.wood-oak{background:linear-gradient(90deg,#c9a264,#dcb77a,#bf955a)}
.wood-gum{background:linear-gradient(90deg,#9a6a43,#b9875e,#8a5c39)}
.photo{position:absolute}
.contact{position:absolute;display:flex;align-items:center;gap:6px;font-size:6px;font-weight:700;color:var(--ink)}
.contact svg{width:14px;height:14px}
.empty-block{position:absolute;background:var(--empty);border-radius:6px}
</style>
</head>
<body>
<div class="canvas">

  <!-- Outside spread: back flap, back cover, front cover -->
  <section class="spread spread--outside">
    <div class="page page--1">
      <div class="band" style="left:0;top:0;width:342px;height:17px"></div>
      <div class="tab tab--left" style="left:180px;width:162px"></div>
      <div class="wordmark wordmark--light" style="left:213px;top:15px;font-size:10px"><i style="width:8px;height:8px"></i>VERIX BOARD</div>
      <h2 class="heading" style="left:29px;top:49px;width:137px">Signage Grade 3MM</h2>
      <div class="grid" style="left:29px;top:82px;row-gap:11px">
        <div class="swatch">High gloss white</div><div class="swatch">High gloss white</div><div class="swatch">High gloss white</div><div class="swatch black dark">High gloss black</div>
        <div class="swatch black dark">High gloss black</div><div class="swatch">High gloss white</div><div class="swatch brush">Brush silver</div><div class="swatch raw">Raw aluminium</div>
        <div class="swatch red dark">High gloss red</div><div class="swatch">High gloss white</div><div class="swatch yellow">High gloss yellow</div><div class="swatch">High gloss white</div>
        <div class="swatch process dark">High gloss process blue</div><div class="swatch">High gloss white</div><div class="swatch reflex dark">High gloss reflex blue</div><div class="swatch">High gloss white</div>
        <div class="swatch forest dark">High gloss forest green</div><div class="swatch">High gloss white</div><div class="swatch heritage dark">High gloss heritage red</div><div class="swatch">High gloss white</div>
        <div class="swatch orange dark">High gloss orange</div><div class="swatch">High gloss white</div><div class="swatch navyblue dark">High gloss navy blue</div><div class="swatch">High gloss white</div>
        <div class="swatch charcoal">Metallic charcoal</div><div class="swatch">High gloss white</div><div class="swatch emerald dark">High gloss emerald green</div><div class="swatch">High gloss white</div>
        <div class="swatch msilver">Metallic silver</div><div class="swatch">High gloss white</div><div class="swatch steel dark">High gloss steel grey</div><div class="swatch">High gloss white</div>
      </div>
      <div class="band" style="left:0;top:468px;width:342px;height:15px"></div>
    </div>

    <div class="page page--2">
      <div class="wordmark wordmark--dark" style="left:27px;top:342px;font-size:15px"><i style="width:12px;height:12px"></i>VERIX BOARD</div>
      <h2 style="position:absolute;left:27px;top:378px;font-size:18px;font-weight:800;color:var(--ink);border-bottom:1.5px solid var(--ink);padding-bottom:1px">GET IN TOUCH</h2>
      <div class="contact" style="left:27px;top:415px">
        <svg viewBox="0 0 14 14"><circle cx="7" cy="7" r="7" fill="var(--navy)"/><path d="M4.6 3.8l1.4 1.6-.8.9a5 5 0 0 0 2.5 2.5l.9-.8 1.6 1.4-.9 1a5.5 5.5 0 0 1-5.7-5.7z" fill="#fff"/></svg>+00 11222 3344 55</div>
      <div class="contact" style="left:124px;top:415px">
        <svg viewBox="0 0 14 14"><circle cx="7" cy="7" r="7" fill="var(--navy)"/><path d="M7 3.2a2.4 2.4 0 0 1 2.4 2.4c0 1.8-2.4 4.6-2.4 4.6S4.6 7.4 4.6 5.6A2.4 2.4 0 0 1 7 3.2z" fill="#fff"/><circle cx="7" cy="5.6" r=".9" fill="var(--navy)"/></svg>your street, city name, country</div>
      <div class="contact" style="left:27px;top:437px">
        <svg viewBox="0 0 14 14"><circle cx="7" cy="7" r="7" fill="var(--navy)"/><path d="M3.5 7.2l7-3.2-2.4 6.6-1.4-2.2z" fill="#fff"/></svg>info.@yourmail.com</div>
      <div class="contact" style="left:124px;top:437px">
        <svg viewBox="0 0 14 14"><circle cx="7" cy="7" r="7" fill="var(--navy)"/><circle cx="7" cy="7" r="3.6" fill="none" stroke="#fff" stroke-width=".8"/><path d="M3.4 7h7.2M7 3.4c-1.6 2-1.6 5.2 0 7.2M7 3.4c1.6 2 1.6 5.2 0 7.2" fill="none" stroke="#fff" stroke-width=".7"/></svg>www.yoursite.com</div>
    </div>

    <div class="page page--3">
      <div class="wordmark wordmark--dark" style="left:109px;top:388px;font-size:18px"><i style="width:14px;height:14px"></i>VERIX BOARD</div>
      <p style="position:absolute;left:109px;top:429px;font-size:12.5px;font-weight:700;color:var(--blue);padding-top:6px;border-top:1px solid var(--blue)">ALUMINIUM COMPOSITE PANEL</p>
      <div style="position:absolute;left:332px;top:391px;width:20px;height:56px;background:var(--blue);clip-path:polygon(40% 0,100% 0,100% 100%,40% 100%,0 50%)"></div>
    </div>

    <svg class="photo" role="img" aria-label="Photograph of a building corner clad in blue composite panels against the sky" style="left:0;top:0" width="1026" height="483" viewBox="0 0 1026 483">
      <defs><linearGradient id="facade" x1="0" y1="0" x2="0" y2="1"><stop offset="0" stop-color="#5a92cf"/><stop offset=".5" stop-color="#2a6fb4"/><stop offset="1" stop-color="#1b568f"/></linearGradient></defs>
      <polygon points="342,0 1026,0 1026,200 684,404 342,207" fill="url(#facade)"/>
    </svg>

    <div style="position:absolute;left:943px;top:0;width:59px;height:91px;background:var(--navy);clip-path:polygon(0 0,100% 0,100% 100%,0 82%)"></div>
    <span style="position:absolute;left:951px;top:28px;font-size:13px;font-weight:600;color:#fff;letter-spacing:.02em">GUIDE</span>
  </section>

  <!-- Inside spread -->
  <section class="spread spread--inside">
    <div class="page page--1" style="background:linear-gradient(180deg,#fff,#eef0f3)">
      <svg class="photo" role="img" aria-label="Collage of modern buildings clad in silver aluminium composite panels" style="left:0;top:0" width="342" height="175" viewBox="0 0 342 175">
        <defs><linearGradient id="collage" x1="0" y1="0" x2="1" y2="1"><stop offset="0" stop-color="#a9b3bf"/><stop offset=".5" stop-color="#c7ccd3"/><stop offset="1" stop-color="#8d949e"/></linearGradient></defs>
        <polygon points="0,17 114,17 114,0 342,0 342,100 270,100 255,175 95,168 95,95 0,95" fill="url(#collage)"/>
      </svg>
      <div class="band" style="left:0;top:0;width:114px;height:17px"></div>
      <div class="wordmark wordmark--dark" style="left:33px;top:190px;font-size:18px"><i style="width:14px;height:14px"></i>VERIX BOARD</div>
      <p style="position:absolute;left:218px;top:190px;font-size:9.5px;font-weight:600;color:var(--ink);line-height:1.1;padding-left:4px;border-left:1px solid var(--ink)">ALUMINIUM<br>COMPOSITE PANEL</p>
      <div class="empty-block" style="left:16px;top:236px;width:151px;height:70px"></div>
      <div class="empty-block" style="left:175px;top:236px;width:151px;height:70px"></div>
      <div class="empty-block" style="left:16px;top:315px;width:151px;height:70px"></div>
      <div class="empty-block" style="left:175px;top:315px;width:151px;height:70px"></div>
      <div class="empty-block" style="left:16px;top:395px;width:151px;height:70px"></div>
      <div class="empty-block" style="left:175px;top:395px;width:151px;height:70px"></div>
    </div>

    <div class="page page--2">
      <h2 class="heading heading--small" style="left:31px;top:63px;width:77px">Light Commercial<br>Grade 3MM</h2>
      <h2 class="heading heading--small" style="left:179px;top:63px;width:128px">Light Commercial Grade<br>SPECIALTY SURFACES</h2>
      <div class="grid" style="left:31px;top:100px;row-gap:7px">
        <div class="swatch">High gloss white</div><div class="swatch">Matte white</div><div class="swatch">Mirror gold</div><div class="swatch undercoat">Undercoat</div>
        <div class="swatch">High gloss white</div><div class="swatch black dark">High gloss black</div><div class="swatch">Mirror silver</div><div class="swatch undercoat">Undercoat</div>
        <div class="swatch black dark">High gloss black</div><div class="swatch black dark">Matte black</div><div class="swatch brush">Brush silver</div><div class="swatch undercoat">Aluminium</div>
      </div>
      <h2 class="heading heading--small" style="left:31px;top:247px;width:199px">Light Commercial Grade OVERSIZED</h2>
      <div class="grid" style="left:31px;top:267px">
        <div class="swatch">High gloss white</div><div class="swatch">Matte white</div><div class="swatch copper">Brush copper</div><div class="swatch gold">Brush gold</div>
      </div>
      <h2 class="heading heading--small" style="left:31px;top:316px;width:256px">Light Commercial Grade SPECIALTY SURFACES</h2>
      <div class="grid" style="left:31px;top:337px;row-gap:7px">
        <div class="swatch embossed">Milled embossed</div><div class="swatch raw">Raw aluminium</div><div class="swatch">Mirror anthracite silver</div><div class="swatch undercoat">Undercoat</div>
        <div class="swatch embossed">Diamond shape embossed</div><div class="swatch raw">Raw aluminium</div><div class="swatch brush">Brush stainless steel</div><div class="swatch">Stainless steel</div>
        <div class="swatch rust dark">Textured rust</div><div class="swatch undercoat">Undercoat</div>
      </div>
    </div>

    <div class="page page--3" style="background:linear-gradient(90deg,#eef2f8,#fff 25%)">
      <h2 class="heading" style="left:29px;top:87px;width:131px">Commercial Grade</h2>
      <h2 class="heading" style="left:176px;top:87px;width:137px">Commercial Grade</h2>
      <div class="grid" style="left:29px;top:110px;row-gap:7px">
        <div class="swatch wood-golden dark">Golden wattle</div><div class="swatch">High gloss white</div><div class="swatch wood-wenge dark">Wenge dark</div><div class="swatch">High gloss white</div>
        <div class="swatch wood-walnut dark">Walnut</div><div class="swatch">High gloss white</div><div class="swatch wood-oak dark">Sorrento oak</div><div class="swatch">High gloss white</div>
        <div class="swatch wood-allspice dark">Vintage allspice</div><div class="swatch">High gloss white</div><div class="swatch wood-gum dark">Sydney spotted gum</div><div class="swatch">High gloss white</div>
      </div>
      <h2 style="position:absolute;left:30px;top:241px;font-size:11.5px;font-weight:600;color:#1d1d1f;white-space:nowrap">Commercial Grade 4MM</h2>
      <div class="grid" style="left:29px;top:267px;row-gap:4px">
        <div class="swatch msilver">PVDF metallic silver</div><div class="swatch">High gloss white</div><div class="swatch black dark">PVDF metallic black</div><div class="swatch undercoat">Undercoat</div>
        <div class="swatch">High gloss white</div><div class="swatch">PVDF matte white</div><div class="swatch black dark">FEVE semi gloss black</div><div class="swatch undercoat">FEVE semi gloss white</div>
        <div class="swatch black dark">High gloss black</div><div class="swatch black dark">PVDF matte black</div>
      </div>
      <svg class="photo" role="img" aria-label="Photograph of a grey panel-clad building with small windows" style="left:89px;top:351px" width="253" height="132" viewBox="0 0 253 132">
        <defs><linearGradient id="bldg" x1="0" y1="0" x2="1" y2="1"><stop offset="0" stop-color="#9aa3ad"/><stop offset=".6" stop-color="#6d7680"/><stop offset="1" stop-color="#c9ced4"/></linearGradient></defs>
        <polygon points="0,132 0,70 40,45 40,40 150,22 235,0 253,40 253,132" fill="url(#bldg)"/>
      </svg>
    </div>

    <div class="band" style="left:342px;top:0;width:684px;height:17px"></div>
    <div class="tab" style="left:524px;width:149px"></div>
    <div class="tab" style="left:686px;width:157px"></div>
    <div class="wordmark wordmark--light" style="left:550px;top:16px;font-size:9.5px"><i style="width:8px;height:8px"></i>VERIX BOARD</div>
    <div class="wordmark wordmark--light" style="left:712px;top:16px;font-size:9.5px"><i style="width:8px;height:8px"></i>VERIX BOARD</div>
  </section>

</div>
</body>
</html>
```